Brightway Freight Biz Card and Stationary
Brightway Freight
Brightway Freight Biz Card and Stationary -
Creative Brief
Modern
Daniel Prescott
President & CEO
P.O. Box 7382 Williston, ND 58217
d.prescott@tarvo.com
keep it simple

```html
<!DOCTYPE html>
<html lang="en">
<head>
<meta charset="utf-8">
<title>Brightway Freight Stationery</title>
<link rel="stylesheet" href="https://fonts.googleapis.com/css2?family=Open+Sans:wght@400;600;700&display=swap">
<style>
:root{
  --bg:#e9e6e1;
  --paper:#ffffff;
  --blue:#1f7ec3;
  --navy:#1d2c44;
  --ink:#333a44;
  --muted:#8a93a0;
  --line:#c9ced6;
  --faint:#e4ecf4;
}
*{box-sizing:border-box;margin:0;padding:0}
html,body{width:1200px;height:608px;overflow:hidden}
body{background:var(--bg);font-family:"Open Sans",Arial,sans-serif;color:var(--ink);position:relative}
.sheet{position:absolute;background:var(--paper);box-shadow:0 2px 6px rgba(0,0,0,.25);overflow:hidden}
.brand{display:flex;align-items:center;gap:6px;justify-content:center}
.brand-dot{border-radius:50%;background:var(--blue);flex:none}
.brand-name{font-weight:700;color:var(--navy);letter-spacing:.5px;text-transform:uppercase;white-space:nowrap}
.watermark{position:absolute;border-radius:50%;background:var(--faint)}
.footer-band{position:absolute;left:0;right:0;bottom:0;height:13px;background:var(--blue);color:#fff;font-size:6.5px;display:flex;align-items:center;justify-content:center;gap:10px;white-space:nowrap}

/* fax */
.fax{left:31px;top:60px;width:353px;height:497px}
.fax .brand{margin-top:16px}
.fax-title{position:absolute;right:14px;top:108px;font-weight:700;font-size:17px;color:var(--navy)}
.fax-table{position:absolute;left:14px;right:14px;top:136px;display:grid;grid-template-columns:1fr 1fr;column-gap:14px;border-top:1px solid var(--line)}
.fax-row{display:flex;align-items:center;height:19px;border-bottom:1px solid var(--line);font-size:7px;color:var(--ink)}
.fax-row span{width:40px}
.fax-checks{position:absolute;left:14px;right:14px;top:218px;display:flex;justify-content:space-between;font-size:7px}
.fax-checks label{display:flex;align-items:center;gap:4px}
.fax-checks i{width:8px;height:8px;border:1px solid var(--muted);display:inline-block}

/* letterhead */
.letter{left:403px;top:60px;width:355px;height:497px}
.letter .brand{margin-top:16px}

/* cards */
.card{width:151px;height:84px;border-radius:4px}
.card-front{left:821px;top:65px}
.card-front .brand{justify-content:flex-start;position:absolute;left:8px;top:8px}
.card-bar{position:absolute;right:0;top:36px;width:70px;height:7px;background:var(--blue)}
.card-info{position:absolute;left:8px;top:36px;font-size:5px;line-height:7px;color:var(--ink)}
.card-info strong{font-size:6px;color:var(--navy)}
.card-back{left:984px;top:65px;display:flex;align-items:center;justify-content:center}

/* envelopes */
.env-front{left:780px;top:163px;width:389px;height:185px}
.env-front .brand{position:absolute;left:16px;top:16px}
.env-addr{position:absolute;left:38px;top:54px;font-size:6px;line-height:8px}
.env-back{left:780px;top:365px;width:389px;height:187px}
.env-flap{position:absolute;left:0;top:0}
.env-back-dot{position:absolute;left:186px;top:20px}
</style>
</head>
<body>

<section class="sheet fax">
  <div class="brand"><span class="brand-dot" style="width:20px;height:20px"></span><span class="brand-name" style="font-size:14px">Brightway Freight</span></div>
  <div class="fax-title">FAX</div>
  <div class="fax-table">
    <div class="fax-row"><span>To:</span></div><div class="fax-row"><span>From:</span></div>
    <div class="fax-row"><span>Fax:</span></div><div class="fax-row"><span>Pages:</span></div>
    <div class="fax-row"><span>Phone:</span></div><div class="fax-row"><span>Date:</span></div>
    <div class="fax-row"><span>Re:</span></div><div class="fax-row"><span>CC:</span></div>
  </div>
  <div class="fax-checks">
    <label><i></i>Urgent</label><label><i></i>For Review</label><label><i></i>Please Comment</label><label><i></i>Please Reply</label><label><i></i>Please Recycle</label>
  </div>
  <div class="watermark" role="img" aria-label="Faint brand mark" style="left:98px;top:285px;width:150px;height:150px"></div>
  <div class="footer-band"><span>P.O. Box 7382 Williston, ND 58217</span><span>T: 701 555 0142</span><span>F: 701 555 0143</span><span>www.tarvo.com</span></div>
</section>

<section class="sheet letter">
  <div class="brand"><span class="brand-dot" style="width:20px;height:20px"></span><span class="brand-name" style="font-size:14px">Brightway Freight</span></div>
  <div class="watermark" role="img" aria-label="Faint brand mark" style="left:86px;top:165px;width:150px;height:150px"></div>
  <div class="footer-band"><span>P.O. Box 7382 Williston, ND 58217</span><span>T: 701 555 0142</span><span>F: 701 555 0143</span><span>www.tarvo.com</span></div>
</section>

<section class="sheet card card-front">
  <div class="brand"><span class="brand-dot" style="width:12px;height:12px"></span><span class="brand-name" style="font-size:8px">Brightway Freight</span></div>
  <div class="card-bar"></div>
  <div class="card-info">
    <strong>Daniel Prescott</strong><br>President &amp; CEO<br>T: 701 555 0142<br>F: 701 555 0143<br>d.prescott@tarvo.com
  </div>
</section>

<section class="sheet card card-back">
  <span class="brand-dot" style="width:24px;height:24px"></span>
</section>

<section class="sheet env-front">
  <div class="brand"><span class="brand-dot" style="width:18px;height:18px"></span><span class="brand-name" style="font-size:13px">Brightway Freight</span></div>
  <div class="env-addr">P.O. Box 7382<br>Williston, ND 58217</div>
  <div class="watermark" role="img" aria-label="Faint brand mark" style="left:289px;top:42px;width:72px;height:72px"></div>
</section>

<section class="sheet env-back">
  <svg class="env-flap" width="389" height="60" viewBox="0 0 389 60">
    <path d="M0 0 H389 V18 Q194 62 0 18 Z" fill="#f4f6f9" stroke="#d3d8df"/>
    <rect x="0" y="0" width="389" height="4" fill="#1f7ec3"/>
  </svg>
  <span class="brand-dot env-back-dot" style="width:18px;height:18px"></span>
</section>

</body>
</html>
```